Brand New Church Business Card Design. Needs to appeal to high school students, professionals.

Business Card. Bold lines and colors. Simple font. This is a new church looking to attract new families who have moved to the area. Business professionals mostly. have a working logo. may need a little tweaking. Church is designed to do excellent ministries for students and children. Like business card design in box on mark vault homepage. Want a front and back side. Prefer colors to match the logo. But will lean on designers preferences and wisdom. DO NOT WANT A CROSS OR RELIGIOUS SYMBOL on the card.

Target Market(s)

Families, Professionals, Students

Industry/Entity Type

High School

Contact Information for Business Card

SaltRock ChurchSaltRock.atForrest Coulter904-515-8349Forrest@PineHollow.at

Font styles to use
Sans Serif

Colors
0255a3
ffffff

Requirements
Must have
• Bold colors. Very Masculine. Creative
Nice to have
• On printnook.markvault.com homepage in the business card design box. the card with the black, blue and gray looks really sharp. matches our logos.
Should not have
• no crosses or religious symbols.

```html
<!DOCTYPE html>
<html lang="en">
<head>
<meta charset="utf-8">
<title>PineHollow Church – Business Card</title>
<link href="https://fonts.googleapis.com/css2?family=Roboto:wght@400;900&display=swap" rel="stylesheet">
<style>
  :root {
    --stage: #e9e6e1;
    --card-black: #0b0c0e;
    --card-black-edge: #1d1f23;
    --card-white: #f7f7f7;
    --card-grey: #dcdcdc;
    --brand-blue: #2f96d2;
    --brand-blue-deep: #0255a3;
    --ink: #111111;
    --ink-soft: #5a5a5a;
    --white: #ffffff;
  }
  * { margin: 0; padding: 0; box-sizing: border-box; }
  html, body {
    width: 1200px; height: 1023px; overflow: hidden;
    background: var(--stage);
    font-family: "Roboto", Arial, sans-serif;
  }
  .canvas { position: relative; width: 1200px; height: 1023px; }
  .card {
    position: absolute; width: 580px; height: 331px;
    border-radius: 6px; overflow: hidden;
    box-shadow: 0 14px 30px rgba(0,0,0,.25);
  }
  .card-front {
    left: 70px; top: 110px;
    background: linear-gradient(160deg, var(--card-black-edge), var(--card-black) 60%);
  }
  .card-back { left: 550px; top: 580px; background: var(--card-white); }

  .front-brand {
    position: absolute; left: 0; top: 0; width: 100%; height: 100%;
    display: flex; align-items: center; justify-content: center; gap: 26px;
  }
  .brand-disc {
    width: 150px; height: 150px; border-radius: 50%;
    background: linear-gradient(135deg, var(--brand-blue), var(--brand-blue-deep));
    flex: none;
  }
  .brand-name {
    font-weight: 900; font-size: 44px; line-height: 1.05;
    color: var(--white); letter-spacing: -0.5px;
  }

  .back-swoosh { position: absolute; inset: 0; }
  .back-disc {
    position: absolute; left: 60px; top: 72px;
    width: 186px; height: 186px; border-radius: 50%;
    background: linear-gradient(135deg, var(--brand-blue-deep), var(--brand-blue));
  }
  .contact {
    position: absolute; left: 310px; top: 92px;
    color: var(--ink-soft); font-size: 17px; line-height: 1.55;
  }
  .contact-name-line { font-weight: 900; font-size: 24px; color: var(--ink); margin-bottom: 10px; }
</style>
</head>
<body>
<main class="canvas">
  <section class="card card-front" aria-label="Card front">
    <div class="front-brand">
      <span class="brand-disc" aria-hidden="true"></span>
      <span class="brand-name">PineHollow<br>Church</span>
    </div>
  </section>

  <section class="card card-back" aria-label="Card back">
    <svg class="back-swoosh" viewBox="0 0 580 331" aria-hidden="true">
      <path d="M260 331 C300 180 420 90 580 60 L580 331 Z" fill="var(--card-grey)" opacity=".55"/>
      <path d="M330 331 C360 230 450 160 580 140 L580 331 Z" fill="var(--card-grey)" opacity=".6"/>
    </svg>
    <span class="back-disc" aria-hidden="true"></span>
    <div class="contact">
      <p class="contact-name-line">PineHollow Church</p>
      <p>904-555-0172</p>
      <p>Dwayne@PineHollow.at</p>
      <p>PineHollow.at</p>
      <p>Dwayne Pellish</p>
    </div>
  </section>
</main>
</body>
</html>
```